Business Card Design

We need a basic, but modern design card. Our business is a local Queanbeyan/Canberra courier service, but can organise interstate delivery if needed. Our fleet ranges from 1 tonne vans to 8 tonne trucks.

Industry/Entity Type

Business

Contact Information for Business Card

Harbourline Freight
14 Wren Parade
Queanbeyan NSW 2620

Dean Fairley
CEO

Phone: 02 61847315
Fax: 02 61847358
email: dean@harbourlinefreight.example.au

```html
<!DOCTYPE html>
<html lang="en">
<head>
<meta charset="utf-8">
<title>Harbourline Freight — Business Card</title>
<link rel="stylesheet" href="https://fonts.googleapis.com/css2?family=Arimo:wght@400;700&display=swap">
<style>
  :root {
    --cardboard-light: #d7b98c;
    --cardboard-mid: #c9a677;
    --cardboard-dark: #b8925f;
    --paper: #ffffff;
    --paper-shade: #f1efec;
    --brand-blue: #1f4aa0;
    --text-blue: #1d3f8f;
    --accent-orange: #e8532a;
    --truck-body: #e9ecef;
    --truck-shade: #aab1b9;
  }
  html, body {
    margin: 0;
    padding: 0;
    overflow: hidden;
    background: #ffffff;
  }
  .card {
    position: relative;
    width: 1200px;
    height: 741px;
    overflow: hidden;
    font-family: "Arimo", Arial, sans-serif;
  }
  .cardboard {
    position: absolute;
    inset: 0;
    background: linear-gradient(160deg, var(--cardboard-light) 0%, var(--cardboard-mid) 55%, var(--cardboard-dark) 100%);
  }
  .torn-paper {
    position: absolute;
    inset: 0;
    width: 1200px;
    height: 741px;
  }
  .brand-name {
    position: absolute;
    left: 75px;
    top: 232px;
    width: 470px;
    margin: 0;
    font-weight: 700;
    font-size: 66px;
    line-height: 1.02;
    color: var(--brand-blue);
    letter-spacing: -0.5px;
  }
  .divider {
    position: absolute;
    left: 584px;
    top: 203px;
    width: 3px;
    height: 286px;
    background: var(--text-blue);
  }
  .contact-list {
    position: absolute;
    left: 614px;
    top: 222px;
    margin: 0;
    padding: 0;
    list-style: none;
    color: var(--text-blue);
    font-size: 29px;
    line-height: 42px;
  }
  .contact-item {
    display: flex;
    align-items: flex-start;
    margin-bottom: 14px;
  }
  .contact-icon {
    width: 28px;
    height: 28px;
    margin: 6px 16px 0 0;
    flex: none;
  }
  .truck-photo {
    position: absolute;
    left: 868px;
    top: 570px;
    width: 272px;
    height: 150px;
    border-radius: 10px 10px 6px 6px;
    background: linear-gradient(180deg, var(--truck-body) 0%, var(--truck-body) 70%, var(--truck-shade) 100%);
  }
</style>
</head>
<body>
<main class="card">
  <div class="cardboard" role="img" aria-label="Corrugated cardboard texture background"></div>

  <svg class="torn-paper" viewBox="0 0 1200 741" aria-hidden="true">
    <path fill="var(--paper)" d="M0 150 L60 146 L140 152 L230 144 L330 150 L420 140 L520 138 L600 128 L700 112 L800 96 L900 84 L1000 76 L1100 70 L1200 64 L1200 560 L1140 548 L1080 540 L1020 526 L960 520 L880 512 L800 508 L720 505 L640 502 L560 500 L480 497 L400 494 L320 492 L240 488 L160 486 L80 480 L0 476 Z"/>
    <path fill="var(--paper-shade)" d="M0 476 L80 480 L160 486 L240 488 L320 492 L400 494 L480 497 L560 500 L640 502 L720 505 L800 508 L880 512 L960 520 L1020 526 L1080 540 L1140 548 L1200 560 L1200 566 L1140 555 L1080 547 L1020 533 L960 527 L880 519 L800 515 L720 512 L640 509 L560 507 L480 504 L400 501 L320 499 L240 495 L160 493 L80 487 L0 483 Z"/>
  </svg>

  <h1 class="brand-name">Harbourline<br>Freight</h1>

  <div class="divider"></div>

  <ul class="contact-list">
    <li class="contact-item">
      <svg class="contact-icon" viewBox="0 0 24 24" aria-hidden="true">
        <path fill="var(--accent-orange)" d="M12 3 L2 12 H5 V21 H10 V15 H14 V21 H19 V12 H22 Z"/>
      </svg>
      <span>14 Wren Parade Queanbeyan NSW<br>2620 Dean Fairley CEO</span>
    </li>
    <li class="contact-item">
      <svg class="contact-icon" viewBox="0 0 24 24" aria-hidden="true">
        <path fill="var(--accent-orange)" d="M6.6 10.8c1.4 2.8 3.8 5.1 6.6 6.6l2.2-2.2c.3-.3.7-.4 1-.2 1.1.4 2.3.6 3.6.6.6 0 1 .4 1 1V20c0 .6-.4 1-1 1C10.6 21 3 13.4 3 4c0-.6.4-1 1-1h3.5c.6 0 1 .4 1 1 0 1.3.2 2.5.6 3.6.1.3 0 .7-.2 1z"/>
      </svg>
      <span>02 61847315</span>
    </li>
    <li class="contact-item">
      <svg class="contact-icon" viewBox="0 0 24 24" aria-hidden="true">
        <g fill="none" stroke="var(--accent-orange)" stroke-width="2">
          <rect x="6" y="3" width="12" height="6"/>
          <rect x="3" y="9" width="18" height="8" rx="1"/>
          <rect x="6" y="14" width="12" height="7"/>
        </g>
      </svg>
      <span>02 61847358</span>
    </li>
    <li class="contact-item">
      <svg class="contact-icon" viewBox="0 0 24 24" aria-hidden="true">
        <g fill="none" stroke="var(--accent-orange)" stroke-width="2">
          <rect x="3" y="6" width="18" height="13"/>
          <path d="M3 6 L12 13 L21 6"/>
        </g>
      </svg>
      <span>dean@harbourlinefreight.example.au</span>
    </li>
  </ul>

  <div class="truck-photo" role="img" aria-label="Photo of a white company box truck"></div>
</main>
</body>
</html>
```